Business Card Design for digital storytelling business

I need a business card for a workshop/consulting/coaching business.

Company Name: Bright Harbor Works

Tagline: New ways to keep old memories close

What we do: Through workshops, webinars, and coaching we teach you how to capture, tell and share your important memories and stories using readily available digital tools. We will help you tell your life story in a format to share with your family now and in the future.
Updates

I just received a toll free number that I would like included on the designs. If the addition of a phone number would significantly alter your design, please submit an altered version. The number is 866-217-9086

Target Market(s)

Adults in US between ages of 35-70 interested in capturing, preserving and sharing memories and life stories in a digital format.
Could include the following:

-People touched by illness or tragedy who need to tell their own or a loved one's life story
-Grandparents wanting to share stories and wisdom with grandchildren living far away
-People with aging parents who want to capture their stories in a format to pass on to their children
-Alzheimer's patients and their families
-People wanting to transfer analog photos to digital; or wanting to organize digital photos into something that tells a story

Industry/Entity Type

Digital

Requirements
Must have
• Must include business name, logo, tagline

Contact information (see file)
Social media information

Fonts easily readable by aging eyes. Good contrast.

Nice to have
• Color preferences: blue, green, yellow/gold
Blue denotes the calm, non-pressured way that I teach. It is for the healing that comes from telling your story. It represents time and space that are bridged in the digital environment.
Green is for growth, the future, the family tree, Vines that grow and branch and connect the generations and our hearts.
Yellow/gold is for the legacy of wisdom in our lives and stories. It is for the light of truth we bring to the world by sharing our stories.
Should not have
• No old-style, script fonts.
No Times New Roman

```html
<!DOCTYPE html>
<html lang="en">
<head>
<meta charset="utf-8">
<title>Bright Harbor Works – Business Card</title>
<link href="https://fonts.googleapis.com/css2?family=Open+Sans:wght@400;600;700&display=swap" rel="stylesheet">
<style>
  :root{
    --backdrop:#d9d6d0;
    --navy:#1c2f5e;
    --navy-deep:#142347;
    --gold:#c9a227;
    --gold-light:#a98407;
    --gold-dark:#6e5200;
    --white:#ffffff;
    --ink:#1f3a78;
    --role:#e9dcb0;
    --icon:#f3e7bd;
    --social-a:#3b5998;
    --social-b:#c0392b;
    --social-c:#2fa3d8;
  }
  *{margin:0;padding:0;box-sizing:border-box}
  html,body{width:1200px;height:871px;overflow:hidden}
  body{background:var(--backdrop);position:relative;font-family:"Open Sans",Arial,sans-serif}

  .card{position:absolute;width:600px;height:343px;overflow:hidden;box-shadow:0 6px 18px rgba(0,0,0,.25)}

  /* back of card */
  .card-back{left:70px;top:80px;background:linear-gradient(160deg,var(--navy) 0%,var(--navy-deep) 100%);color:var(--white)}
  .brand{position:absolute;display:flex;align-items:center;gap:12px}
  .card-back .brand{left:46px;top:96px}
  .brand-mark{width:34px;height:34px;border:2px solid var(--gold);border-radius:50%;flex:none}
  .brand-name{font-weight:600;font-size:26px;line-height:1;letter-spacing:.2px;white-space:nowrap}
  .tagline{font-size:9.5px;letter-spacing:.6px;text-transform:uppercase;margin-top:4px;white-space:nowrap}
  .card-back .tagline{color:var(--gold)}
  .social{position:absolute;left:46px;top:182px;list-style:none;font-size:12px;line-height:20px;color:#e6e9f2}
  .social li{display:flex;align-items:center;gap:10px}
  .social .dot{width:11px;height:11px;display:inline-block}
  .dot-a{background:var(--social-a)} .dot-b{background:var(--social-b)} .dot-c{background:var(--social-c)}

  /* front of card */
  .card-front{left:530px;top:448px;display:flex;background:var(--white)}
  .front-brand{position:relative;width:330px;height:100%;background:linear-gradient(180deg,#fff 60%,#f1f1f1 100%)}
  .front-brand .brand{left:26px;top:34px}
  .front-brand .brand-mark{border-color:var(--ink)}
  .front-brand .brand-name{color:var(--ink);font-size:24px}
  .front-brand .tagline{color:var(--ink);font-size:8.5px}
  .divider{width:10px;height:100%;background:var(--ink)}
  .contact{flex:1;background:linear-gradient(150deg,var(--gold-light) 0%,#8a6a02 60%,var(--gold-dark) 100%);color:var(--white);padding:92px 0 0 24px;font-size:13px;line-height:19px}
  .person-name{font-weight:700;font-size:17px;color:var(--ink);margin-left:22px}
  .person-role{font-size:11.5px;color:var(--role);margin-left:22px;margin-bottom:10px}
  .mail-label{font-weight:600}
  .contact-line{display:flex;align-items:center;gap:10px;margin-top:2px}
  .contact-line svg{flex:none}
  .address{margin-bottom:8px}
</style>
</head>
<body>

<section class="card card-back" aria-label="Card back">
  <div class="brand">
    <span class="brand-mark"></span>
    <div>
      <div class="brand-name">Bright Harbor Works</div>
      <div class="tagline">New ways to keep old memories close</div>
    </div>
  </div>
  <ul class="social">
    <li><span class="dot dot-a"></span>www.brightharborworks.com/circle</li>
    <li><span class="dot dot-b"></span>www.brightharborworks.com/boards/</li>
    <li><span class="dot dot-c"></span>@BrightHarborW</li>
  </ul>
</section>

<section class="card card-front" aria-label="Card front">
  <div class="front-brand">
    <div class="brand">
      <span class="brand-mark"></span>
      <div>
        <div class="brand-name">Bright Harbor Works</div>
        <div class="tagline">New ways to keep old memories close</div>
      </div>
    </div>
  </div>
  <div class="divider"></div>
  <div class="contact">
    <div class="person-name">Maren Holloway</div>
    <div class="person-role">Founder</div>
    <div class="mail-label">Mail:</div>
    <div class="address">PO Box 218<br>Millbrook, RI 02904</div>
    <div class="contact-line">
      <svg width="12" height="10" viewBox="0 0 12 10" aria-hidden="true"><rect x=".5" y=".5" width="11" height="9" fill="none" stroke="var(--icon)"/><path d="M.5 .5 6 5.5 11.5 .5" fill="none" stroke="var(--icon)"/></svg>
      maren@brightharborworks.com
    </div>
    <div class="contact-line">
      <svg width="12" height="12" viewBox="0 0 12 12" aria-hidden="true"><circle cx="6" cy="6" r="5.3" fill="none" stroke="var(--icon)"/><ellipse cx="6" cy="6" rx="2.3" ry="5.3" fill="none" stroke="var(--icon)"/><path d="M.7 6h10.6" stroke="var(--icon)"/></svg>
      www.brightharborworks.com
    </div>
  </div>
</section>

</body>
</html>
```